Emmy award winning Hollywood sound studio needs a cool website

We need a website designed and coded to showcase our company and talent to our current and future clients. We are a post-production sound studio that works with Brambletoon, Vidora, Calder Sisters, Glimmerforge, and other major Hollywood studios and companies. We primarily work designing sound effects for animated TV shows like Puddlefin McGee, Rookie Rangers Roll!, Tiger Dojo: Lantern Riders, Fossil Valley Stampede Files, The Sly Crew, My Aunt the Starship Pilot, Spear of Helix, and the recent Vidora movie Wren and the Quiet. A website for our company would provide basic information about our studio and services, the kinds of projects we are currently working on and have worked on in the past, the awards we have won or been nominated for, and most importantly showcase our talented engineers so that producers and directors can get to know the people they might want to collaborate with. Our studio is located in Burbank, CA right in the heart of where all the studios are located. We have a basic company logo. We don't really have a color scheme to our studio so we're very open and flexible in that department. We have decorated our studio with a bit of an Art Deco style to invoke an old classy movie theater from the golden age of Hollywood. Our lobby resembles the lobby of a movie theater complete with a neon marquee where we post fun sayings or quotes from our shows. I think it would be fun for the website design to reflect that Art Deco/classic movie theater feeling. Another website that I think has a good simple design for inspiration is Fernhollow Audio: "www.fernaudio.example".
Target Market(s)
Major Hollywood Studios, Animation production companies, independent film/TV production
Industry/Entity Type
Hollywood, Television, Streaming, Entertainment, Games
Coding
Coded - Design and coding required
Number of Pages Required
5+ page
Look and feel

```html
<!DOCTYPE html>
<html lang="en">
<head>
<meta charset="utf-8">
<title>Our Team — Echo Outlaws</title>
<link href="https://fonts.googleapis.com/css2?family=Limelight&family=Space+Grotesk:wght@400;500;600;700&display=swap" rel="stylesheet">
<style>
  :root{
    --ink:#0d0d0d;
    --ink-2:#151515;
    --gold:#d4b25a;
    --gold-soft:rgba(212,178,90,.45);
    --white:#ffffff;
    --muted:#9a9a9a;
    --line:#e4e4e4;
    --text:#1a1a1a;
    --soft:#6f6f6f;
    --deco:"Limelight","Georgia",serif;
  }
  *{box-sizing:border-box;margin:0;padding:0}
  html,body{width:733px;height:1200px;overflow:hidden}
  body{font-family:"Space Grotesk",Arial,sans-serif;background:var(--ink);color:var(--white)}
  .page{width:733px;height:1200px;position:relative}

  /* hero */
  .hero{position:relative;height:268px;overflow:hidden}
  .hero-photo{position:absolute;inset:0;background:
      radial-gradient(ellipse at 72% 40%,#4a4f52 0%,#2a2d30 35%,transparent 70%),
      linear-gradient(180deg,#2b2e31 0%,#1d1f21 60%,#121314 100%)}
  .hero-shade{position:absolute;inset:0;background:rgba(0,0,0,.35)}
  .site-header{position:absolute;top:0;left:0;right:0;height:70px;display:flex;align-items:center;padding:0 40px}
  .brand{display:flex;align-items:center;gap:6px;color:var(--gold);font-weight:700;font-size:14px;line-height:1;width:140px}
  .brand-dot{width:10px;height:10px;background:var(--gold)}
  .main-nav{display:flex;gap:16px;margin-left:130px;font-size:11px;font-weight:600}
  .main-nav a{color:var(--white);text-decoration:none}
  .main-nav a.active{border-bottom:1px solid var(--gold);padding-bottom:3px}
  .header-tools{margin-left:auto;display:flex;gap:16px;align-items:center}
  .header-tools svg{display:block}
  .hero-title{position:absolute;top:118px;left:0;right:0;text-align:center}
  .hero-title h1{font-family:var(--deco);font-weight:400;font-size:36px;letter-spacing:1px}
  .deco-rule{display:flex;align-items:center;justify-content:center;gap:6px;margin-top:10px}
  .deco-rule i{display:block;height:1px;width:46px;background:var(--gold)}
  .deco-rule b{display:block;width:6px;height:6px;background:var(--gold);transform:rotate(45deg)}
  .crumbs{font-size:8px;margin-top:8px;letter-spacing:1.5px;text-transform:uppercase}

  /* team */
  .team{height:372px;background:var(--ink);display:flex;justify-content:center;gap:16px;padding-top:44px}
  .member{width:188px}
  .member-frame{padding:4px;border:1px solid var(--gold-soft)}
  .member-photo{height:218px;background:linear-gradient(180deg,#2a2624 0%,#3a302c 55%,#1c1a19 100%)}
  .member h3{font-size:12px;font-weight:700;margin-top:14px}
  .member p{font-size:9px;color:var(--gold);margin-top:4px;letter-spacing:.4px}

  /* contact */
  .contact{height:316px;background:var(--white);color:var(--text);display:flex;padding:52px 70px 0}
  .details{width:190px}
  .details h2{font-family:var(--deco);font-weight:400;font-size:16px}
  .details .addr{font-size:8.5px;line-height:1.6;color:var(--soft);margin-top:20px}
  .details .mail{font-size:8.5px;color:var(--soft);margin-top:12px}
  .details .phone{font-size:10px;font-weight:700;margin-top:10px}
  .socials{display:flex;gap:8px;margin-top:22px}
  .socials span{width:22px;height:22px;border-radius:50%;border:1px solid var(--line);display:flex;align-items:center;justify-content:center}
  .socials span i{width:5px;height:5px;border-radius:50%;background:var(--text)}
  .form{flex:1;margin-left:50px;font-size:9px;color:#9b9b9b}
  .row{display:flex;gap:22px}
  .field{flex:1;height:40px;border-bottom:1px solid var(--line);display:flex;align-items:center;gap:8px;padding-top:4px}
  .field.msg{height:58px;align-items:flex-start;padding-top:16px}
  .form-foot{display:flex;align-items:center;gap:18px;margin-top:20px}
  .btn{background:var(--gold);color:var(--text);font-weight:600;font-size:9px;border-radius:20px;padding:9px 16px;display:flex;align-items:center;gap:6px}
  .btn i{width:7px;height:7px;border-radius:50%;background:var(--text)}
  .agree{display:flex;align-items:center;gap:6px;font-size:7.5px;color:var(--soft)}
  .agree span.box{width:8px;height:8px;border:1px solid #bbb;flex:none}
  .agree u{color:var(--text)}

  /* footer */
  .site-footer{height:244px;background:var(--ink);padding:46px 58px 0;position:relative}
  .cta{font-family:var(--deco);font-weight:400;font-size:24px;line-height:1.25}
  .cta em{display:block;font-style:normal;color:var(--gold)}
  .foot-row{display:flex;align-items:center;margin-top:26px}
  .foot-nav{display:flex;gap:14px;font-size:9px}
  .foot-socials{margin-left:auto;display:flex;gap:10px}
  .foot-socials span{width:22px;height:22px;border-radius:50%;border:1px solid #333;display:flex;align-items:center;justify-content:center}
  .foot-socials span i{width:5px;height:5px;border-radius:50%;background:var(--white)}
  .foot-rule{height:1px;background:#2a2a2a;margin-top:26px}
  .copy{font-size:7.5px;color:var(--muted);margin-top:14px}
  .to-top{position:absolute;right:24px;top:64px;width:22px;height:22px;border-radius:50%;background:var(--gold);display:flex;align-items:center;justify-content:center}
</style>
</head>
<body>
<div class="page">
  <section class="hero">
    <div class="hero-photo" role="img" aria-label="Sound engineer working at a large mixing console in a dim studio"></div>
    <div class="hero-shade"></div>
    <header class="site-header">
      <div class="brand"><span class="brand-dot"></span>Echo Outlaws</div>
      <nav class="main-nav">
        <a href="#">Home</a><a href="#" class="active">Pages</a><a href="#">Blog</a><a href="#">Shop</a><a href="#">Contacts</a>
      </nav>
      <div class="header-tools">
        <svg width="14" height="14" viewBox="0 0 14 14"><path d="M3 4h8l-1 8H4z" fill="none" stroke="#fff" stroke-width="1.3"/><circle cx="11" cy="3" r="2.5" fill="#d4b25a"/></svg>
        <svg width="14" height="14" viewBox="0 0 14 14"><circle cx="6" cy="6" r="4.2" fill="none" stroke="#fff" stroke-width="1.5"/><path d="M9 9l4 4" stroke="#fff" stroke-width="1.5"/></svg>
        <svg width="14" height="14" viewBox="0 0 14 14" fill="#fff"><circle cx="2" cy="2" r="1.4"/><circle cx="7" cy="2" r="1.4"/><circle cx="12" cy="2" r="1.4"/><circle cx="2" cy="7" r="1.4"/><circle cx="7" cy="7" r="1.4"/><circle cx="12" cy="7" r="1.4"/><circle cx="2" cy="12" r="1.4"/><circle cx="7" cy="12" r="1.4"/><circle cx="12" cy="12" r="1.4"/></svg>
      </div>
    </header>
    <div class="hero-title">
      <h1>Our Team</h1>
      <div class="deco-rule"><i></i><b></b><i></i></div>
      <p class="crumbs">Home / Our Team</p>
    </div>
  </section>

  <section class="team">
    <article class="member">
      <div class="member-frame"><div class="member-photo" role="img" aria-label="Portrait of sound engineer Mara Ellison"></div></div>
      <h3>Mara Ellison</h3><p>Sound Engineer</p>
    </article>
    <article class="member">
      <div class="member-frame"><div class="member-photo" role="img" aria-label="Portrait of vocal producer Dorian Wells"></div></div>
      <h3>Dorian Wells</h3><p>Vocal Producer</p>
    </article>
    <article class="member">
      <div class="member-frame"><div class="member-photo" role="img" aria-label="Portrait of songwriter Felix Harlan"></div></div>
      <h3>Felix Harlan</h3><p>Songwriter</p>
    </article>
  </section>

  <section class="contact">
    <div class="details">
      <h2>Contact Details</h2>
      <p class="addr">12 Lantern Row, Suite 40<br>Burbank, CA 91502</p>
      <p class="mail">hello@echooutlaws.example</p>
      <p class="phone">+1 555 014 27 80</p>
      <div class="socials"><span><i></i></span><span><i></i></span><span><i></i></span><span><i></i></span></div>
    </div>
    <form class="form">
      <div class="row">
        <div class="field">
          <svg width="9" height="9" viewBox="0 0 10 10"><circle cx="5" cy="3" r="2" fill="none" stroke="#aaa"/><path d="M1 10c0-3 8-3 8 0" fill="none" stroke="#aaa"/></svg>Name</div>
        <div class="field">
          <svg width="10" height="8" viewBox="0 0 10 8"><rect x=".5" y=".5" width="9" height="7" fill="none" stroke="#aaa"/><path d="M.5 .5l4.5 4 4.5-4" fill="none" stroke="#aaa"/></svg>Email Address</div>
      </div>
      <div class="row">
        <div class="field">
          <svg width="9" height="9" viewBox="0 0 10 10"><path d="M2 1l2 2-1 1.5c1 1.5 2 2.5 3.5 3.5L8 7l2 2-1.5 1C4 9.5 .5 6 0 1.5z" fill="none" stroke="#aaa"/></svg>Phone</div>
        <div class="field">
          <svg width="9" height="9" viewBox="0 0 10 10"><circle cx="5" cy="5" r="4" fill="none" stroke="#aaa"/><path d="M5 3v3" stroke="#aaa"/></svg>Subject</div>
      </div>
      <div class="field msg">
        <svg width="9" height="9" viewBox="0 0 10 10"><path d="M1 9l1-3 5-5 2 2-5 5z" fill="none" stroke="#aaa"/></svg>How can we help you? Feel free to get in touch!</div>
      <div class="form-foot">
        <span class="btn"><i></i>Get In Touch</span>
        <label class="agree"><span class="box"></span>I agree that my submitted data is <u>collected and stored</u>.</label>
      </div>
    </form>
  </section>

  <footer class="site-footer">
    <p class="cta">Ready for your next premiere?<em>Let's make it sound.</em></p>
    <div class="foot-row">
      <nav class="foot-nav"><span>Home</span><span>Services</span><span>About Us</span><span>Features</span><span>Contacts</span></nav>
      <div class="foot-socials"><span><i></i></span><span><i></i></span><span><i></i></span><span><i></i></span></div>
    </div>
    <div class="foot-rule"></div>
    <p class="copy">Echo Outlaws © 2024. All Rights Reserved.</p>
    <span class="to-top"><svg width="8" height="8" viewBox="0 0 8 8"><path d="M4 7V1M1 4l3-3 3 3" fill="none" stroke="#0d0d0d" stroke-width="1.3"/></svg></span>
  </footer>
</div>
</body>
</html>
```